Package Design - Disposable Face Towel

Hi,

We are needing assistance with graphic design on our box/carton/package.

The attached image that is white is our biggest competitor.

Our brand is "BRIGHT DEW LTD." Please see the logo we uploaded.

Oder we have in mind for front of box:

Logo
LARGE TOWELS
50 Count
Ultra Soft| 100% USDA Bio-Based|100% Eucalyptus Viscose | Vegan
BRIGHTDEWLTD.EXAMPLE

We like medium to dark blue on most of the box, with white and minimal hot pink or salmon. Something that is sharp, modern, and stands out from our competitors.

Box dimensions are: 6.25 x 5.25 x 4.75 inches

This will be 1 of many design projects.

Target Market(s)

Female Beauty Products

Font styles to use
Serif
Sans Serif

Colors
0054AA
0677BA
7BADD7
CADEEF
E8F1F8
EB3D1F
EC4F4E
F09395
F8D3D4
FCEDEE

Requirements
Must have
• Needs to look sharp and modern

```html
<!DOCTYPE html>
<html lang="en">
<head>
<meta charset="utf-8">
<title>Bright Dew Ltd. – Large Towels carton</title>
<link href="https://fonts.googleapis.com/css2?family=Montserrat:wght@300;400;500;600;800&display=swap" rel="stylesheet">
<style>
  :root {
    --navy: #2b3a78;
    --navy-deep: #222f66;
    --stage: #3a4f97;
    --stage-dark: #26336a;
    --white: #ffffff;
    --band: #ececee;
    --ink-soft: rgba(255,255,255,0.72);
    --line-soft: rgba(255,255,255,0.55);
  }
  * { box-sizing: border-box; margin: 0; padding: 0; }
  html, body { width: 746px; height: 1200px; overflow: hidden; }
  body { font-family: "Montserrat", sans-serif; background: var(--white); position: relative; }

  .stage {
    position: absolute; left: 0; width: 746px; height: 590px;
    background: radial-gradient(ellipse at 50% 45%, var(--stage) 0%, var(--stage-dark) 100%);
  }
  .stage--first { top: 0; }
  .stage--second { top: 604px; height: 596px; }

  .carton { position: absolute; left: 16px; top: 148px; display: flex; }
  .stage--second .carton { top: 150px; }

  .panel {
    position: relative; height: 295px; overflow: hidden;
    background: linear-gradient(160deg, var(--navy) 0%, var(--navy-deep) 100%);
    color: var(--white);
  }
  .panel--side { width: 326px; }
  .panel--front { width: 388px; border-left: 1px solid rgba(255,255,255,0.08); }

  /* side panel */
  .about { position: absolute; left: 18px; top: 20px; width: 290px; }
  .about__title { font-weight: 300; font-size: 13px; letter-spacing: 0.2px; margin-bottom: 10px; }
  .about__body { font-size: 5.2px; line-height: 8.6px; text-align: justify; color: var(--ink-soft); text-transform: uppercase; margin-bottom: 6px; }
  .side-url { position: absolute; left: 0; right: 0; text-align: center; font-size: 7px; line-height: 9px; font-weight: 300; }

  /* front panel */
  .window {
    position: absolute; left: 24px; top: 4px; width: 340px; height: 150px;
    border: 1px dashed var(--line-soft); border-top: none;
  }
  .brand {
    position: absolute; left: 40px; top: 48px; width: 308px; text-align: center;
    font-weight: 300; font-size: 24px; letter-spacing: 1px; white-space: nowrap;
  }
  .pill {
    position: absolute; left: 90px; top: 176px; width: 208px; height: 36px;
    border: 2px solid var(--white); border-radius: 18px; padding: 2px;
  }
  .pill__inner {
    width: 100%; height: 100%; background: var(--white); border-radius: 15px;
    color: var(--navy); font-weight: 500; font-size: 15px; letter-spacing: 0.5px;
    display: flex; align-items: center; justify-content: center;
  }
  .tagline { position: absolute; left: 0; right: 0; text-align: center; font-size: 4.4px; line-height: 7px; color: var(--ink-soft); text-transform: uppercase; }
  .front-url { position: absolute; left: 0; right: 0; text-align: center; font-size: 8px; line-height: 10px; font-weight: 400; letter-spacing: 0.3px; }

  /* claims band */
  .band {
    position: absolute; left: 0; right: 0; bottom: 0;
    background: linear-gradient(180deg, var(--white) 0%, var(--band) 100%);
    color: var(--navy); display: flex; align-items: center; justify-content: space-around; padding: 0 10px;
  }
  .band--claims { height: 48px; }
  .count { text-align: center; line-height: 1; }
  .count__num { font-weight: 800; font-size: 22px; }
  .count__label { font-size: 6.5px; font-weight: 400; line-height: 7.5px; }
  .claim { text-align: center; line-height: 1; display: flex; flex-direction: column; align-items: center; }
  .claim__icon { width: 12px; height: 12px; margin-bottom: 3px; }
  .claim__main { font-size: 5.5px; font-weight: 600; }
  .claim__sub { font-size: 3.6px; font-weight: 400; margin-top: 1px; letter-spacing: 0.3px; }

  .panel--side .band { padding: 0 6px; }
  .panel--side .count__num { font-size: 18px; }

  /* second variant: taller band holding the address */
  .band--tall { height: 68px; }
  .band--tall .band__row { display: flex; align-items: center; justify-content: space-around; width: 100%; }
  .band--stack { flex-direction: column; justify-content: center; gap: 4px; }
  .band__url { font-size: 6px; font-weight: 400; color: var(--navy); }
  .band--side-url { font-size: 7px; font-weight: 300; }
  .claim--small .claim__icon { width: 10px; height: 10px; }
  .claim--small .claim__main { font-size: 4.6px; }
</style>
</head>
<body>

<section class="stage stage--first">
  <div class="carton">
    <div class="panel panel--side">
      <div class="about">
        <h2 class="about__title">ABOUT THE TOWEL</h2>
        <p class="about__body">Lorem ipsum dolor sit amet, consectetuer adipiscing elit, sed diam nonummy nibh euismod tincidunt ut laoreet dolore magna aliquam erat volutpat. Ut wisi enim ad minim veniam, quis nostrud exerci tation ullamcorper suscipit lobortis nisl ut aliquip ex ea commodo consequat. Duis autem vel eum iriure dolor in hendrerit in vulputate velit esse molestie consequat, vel illum dolore eu feugiat nulla facilisis at vero eros et accumsan et iusto odio dignissim qui blandit praesent luptatum zzril delenit augue duis dolore te feugait nulla facilisi.</p>
        <p class="about__body">Lorem ipsum dolor sit amet, cons ectetuer adipiscing elit, sed diam nonummy nibh euismod tincidunt ut laoreet dolore magna aliquam erat volutpat. Ut wisi enim ad minim veniam.</p>
        <p class="about__body">Lorem ipsum dolor sit amet, cons ectetuer adipiscing elit, sed diam nonummy nibh euismod tincidunt ut laoreet dolore magna aliquam erat volutpat. Ut wisi enim ad minim veniam.</p>
      </div>
      <p class="side-url" style="top:228px">BRIGHTDEWLTD.EXAMPLE</p>
      <div class="band band--claims">
        <div class="count"><div class="count__num">50</div><div class="count__label">COUNT<br>TOWELS</div></div>
        <div class="claim"><svg class="claim__icon" role="img" aria-label="Feather icon"><circle cx="6" cy="6" r="5" fill="currentColor"/></svg><span class="claim__main">ULTRA</span><span class="claim__sub">SOFT</span></div>
        <div class="claim"><svg class="claim__icon" role="img" aria-label="Bio-based icon"><circle cx="6" cy="6" r="5" fill="currentColor"/></svg><span class="claim__main">100%</span><span class="claim__sub">USDA<br>BIO-BASED</span></div>
        <div class="claim"><svg class="claim__icon" role="img" aria-label="Eucalyptus icon"><circle cx="6" cy="6" r="5" fill="currentColor"/></svg><span class="claim__main">100%</span><span class="claim__sub">EUCALYPTUS<br>VISCOSE</span></div>
        <div class="claim"><svg class="claim__icon" role="img" aria-label="Vegan icon"><circle cx="6" cy="6" r="5" fill="currentColor"/></svg><span class="claim__main">100%</span><span class="claim__sub">VEGAN</span></div>
      </div>
    </div>

    <div class="panel panel--front">
      <div class="window"></div>
      <p class="brand">BRIGHT DEW LTD.</p>
      <div class="pill"><div class="pill__inner">LARGE TOWELS</div></div>
      <p class="tagline" style="top:216px">Usable in both dry and wet cases<br>with great performance in water absorption and retention</p>
      <p class="front-url" style="top:233px">BRIGHTDEWLTD.EXAMPLE</p>
      <div class="band band--claims">
        <div class="count"><div class="count__num">50</div><div class="count__label">COUNT<br>TOWELS</div></div>
        <div class="claim"><svg class="claim__icon" role="img" aria-label="Feather icon"><circle cx="6" cy="6" r="5" fill="currentColor"/></svg><span class="claim__main">ULTRA</span><span class="claim__sub">SOFT</span></div>
        <div class="claim"><svg class="claim__icon" role="img" aria-label="Bio-based icon"><circle cx="6" cy="6" r="5" fill="currentColor"/></svg><span class="claim__main">100%</span><span class="claim__sub">USDA<br>BIO-BASED</span></div>
        <div class="claim"><svg class="claim__icon" role="img" aria-label="Eucalyptus icon"><circle cx="6" cy="6" r="5" fill="currentColor"/></svg><span class="claim__main">100%</span><span class="claim__sub">EUCALYPTUS<br>VISCOSE</span></div>
        <div class="claim"><svg class="claim__icon" role="img" aria-label="Vegan icon"><circle cx="6" cy="6" r="5" fill="currentColor"/></svg><span class="claim__main">100%</span><span class="claim__sub">VEGAN</span></div>
      </div>
    </div>
  </div>
</section>

<section class="stage stage--second">
  <div class="carton">
    <div class="panel panel--side">
      <div class="about">
        <h2 class="about__title">ABOUT THE TOWEL</h2>
        <p class="about__body">Lorem ipsum dolor sit amet, consectetuer adipiscing elit, sed diam nonummy nibh euismod tincidunt ut laoreet dolore magna aliquam erat volutpat. Ut wisi enim ad minim veniam, quis nostrud exerci tation ullamcorper suscipit lobortis nisl ut aliquip ex ea commodo consequat. Duis autem vel eum iriure dolor in hendrerit in vulputate velit esse molestie consequat, vel illum dolore eu feugiat nulla facilisis at vero eros et accumsan et iusto odio dignissim qui blandit praesent luptatum zzril delenit augue duis dolore te feugait nulla facilisi.</p>
        <p class="about__body">Lorem ipsum dolor sit amet, cons ectetuer adipiscing elit, sed diam nonummy nibh euismod tincidunt ut laoreet dolore magna aliquam erat volutpat. Ut wisi enim ad minim veniam.</p>
        <p class="about__body">Lorem ipsum dolor sit amet, cons ectetuer adipiscing elit, sed diam nonummy nibh euismod tincidunt ut laoreet dolore magna aliquam erat volutpat. Ut wisi enim ad minim veniam.</p>
      </div>
      <div class="band band--tall band--side-url">BRIGHTDEWLTD.EXAMPLE</div>
    </div>

    <div class="panel panel--front">
      <div class="window"></div>
      <p class="brand">BRIGHT DEW LTD.</p>
      <div class="pill" style="top:168px"><div class="pill__inner">LARGE TOWELS</div></div>
      <p class="tagline" style="top:208px;font-size:5px;line-height:8px">Usable in both dry and wet cases<br>with great performance in water absorption and retention</p>
      <div class="band band--tall band--stack">
        <div class="band__row">
          <div class="count"><div class="count__num">50</div><div class="count__label">COUNT<br>TOWELS</div></div>
          <div class="claim claim--small"><svg class="claim__icon" role="img" aria-label="Feather icon"><circle cx="5" cy="5" r="4" fill="currentColor"/></svg><span class="claim__main">ULTRA</span><span class="claim__sub">SOFT</span></div>
          <div class="claim claim--small"><svg class="claim__icon" role="img" aria-label="Bio-based icon"><circle cx="5" cy="5" r="4" fill="currentColor"/></svg><span class="claim__main">100%</span><span class="claim__sub">USDA<br>BIO-BASED</span></div>
          <div class="claim claim--small"><svg class="claim__icon" role="img" aria-label="Eucalyptus icon"><circle cx="5" cy="5" r="4" fill="currentColor"/></svg><span class="claim__main">100%</span><span class="claim__sub">EUCALYPTUS<br>VISCOSE</span></div>
          <div class="claim claim--small"><svg class="claim__icon" role="img" aria-label="Vegan icon"><circle cx="5" cy="5" r="4" fill="currentColor"/></svg><span class="claim__main">100%</span><span class="claim__sub">VEGAN</span></div>
        </div>
        <p class="band__url">BRIGHTDEWLTD.EXAMPLE</p>
      </div>
    </div>
  </div>
</section>

</body>
</html>
```